Business Card Design

We need a modern sleek luxury design.
Updates

Low design quality

Want to see business card design. Logo design has been unsuccessful. Please design a sleek modern simple business card

Target Market(s)

People looking to buy or sell their homes. age range from 24-60

Industry/Entity Type

Real Estate

Logo Text

The Penwarden Real Estate Group

Logo styles of interest
Abstract Logo
Lettermark Logo
Font styles to use
Other font styles liked:
• not sure

Colors

Designer to choose colors to be used in the design.

Requirements
Must have
• Want the gold to be able to print as foil
Should not have
• attached are the previous logo designs before we rebranded.

```html
<!DOCTYPE html>
<html lang="en">
<head>
<meta charset="UTF-8">
<title>The Penwarden Real Estate Group — Business Card</title>
<link rel="stylesheet" href="https://fonts.googleapis.com/css2?family=Montserrat:wght@500&display=swap">
<style>
  :root {
    --paper: #ffffff;
    --ink: #000000;
    --gold: #d4ab3f;
  }
  html, body {
    margin: 0;
    padding: 0;
    width: 720px;
    height: 1200px;
    overflow: hidden;
    background: var(--paper);
  }
  .card {
    position: relative;
    width: 720px;
    height: 1200px;
    background: var(--paper);
    overflow: hidden;
  }
  .brush-field {
    position: absolute;
    inset: 0;
    width: 720px;
    height: 1200px;
  }
  .brush-field path { fill: var(--ink); }
  .brand-mark {
    position: absolute;
    left: 112px;
    top: 480px;
    width: 132px;
    height: 132px;
    box-sizing: border-box;
    border: 13px solid var(--gold);
    border-radius: 50%;
  }
  .brand {
    position: absolute;
    left: 272px;
    top: 556px;
    font-family: "Montserrat", sans-serif;
    font-weight: 500;
    color: var(--gold);
  }
  .brand-name {
    margin: 0;
    font-size: 38px;
    line-height: 46px;
    font-weight: 500;
    letter-spacing: 0.5px;
    white-space: nowrap;
  }
  .brand-tagline {
    margin: 6px 0 0 10px;
    font-size: 18px;
    line-height: 22px;
    letter-spacing: 3.5px;
    text-transform: uppercase;
    font-weight: 500;
    white-space: nowrap;
  }
</style>
</head>
<body>
  <main class="card">
    <svg class="brush-field" viewBox="0 0 720 1200" aria-hidden="true">
      <path d="M60 60 C70 40 90 30 110 48 L130 35 C150 20 170 42 190 30 L205 72 C215 50 240 40 260 60
               C270 45 300 30 320 55 L345 40 C370 60 390 30 410 55 L430 25 C450 15 470 40 480 55
               L505 35 C520 50 540 25 560 48 L575 70 C590 40 610 45 625 60 L650 45 C670 70 690 60 680 95
               L700 130 C690 180 705 230 690 280 L705 340 C695 420 710 500 695 580 L705 650
               C690 740 705 820 692 900 L700 960 C690 1010 700 1050 680 1080
               L690 1110 C670 1130 650 1100 630 1125 L610 1160 C590 1140 570 1150 550 1125
               L520 1165 C500 1140 470 1150 450 1130 L420 1170 C400 1150 380 1160 360 1135
               L330 1165 C310 1140 290 1150 270 1125 L240 1160 C220 1140 200 1150 185 1120
               L160 1155 C140 1130 120 1140 100 1110 L80 1135 C60 1110 50 1090 40 1070
               L28 1020 C40 960 22 900 35 840 L25 760 C38 680 22 600 34 520
               L24 440 C36 360 22 280 34 200 L28 140 C34 110 45 80 60 60 Z"/>
    </svg>

    <div class="brand-mark" aria-hidden="true"></div>
    <header class="brand">
      <h1 class="brand-name">The Penwarden</h1>
      <p class="brand-tagline">Real Estate Group</p>
    </header>
  </main>
</body>
</html>
```